Company web site

Looking for a full responsive(mobile friendly) wordpress implementation

Some material is in the website -- brivanta.examplesite.test

But looking for a template more consistent with the logo design, and more future looking.

Target Market(s)

Enterprise Clients

Industry/Entity Type

It Company

Font styles to use
Sans Serif

Colors
33a6d7
0255a3
0455a3
cfdeed
85abd2
3176b5

Requirements
Must have
• about, contact information, partner page, success stories, customer testimonials. links to social presence.
• pricing information

```html
<!DOCTYPE html>
<html lang="en">
<head>
<meta charset="utf-8">
<title>Brivanta — IoT Cloud &amp; Enterprise Software</title>
<link rel="stylesheet" href="https://fonts.googleapis.com/css2?family=Lato:wght@400;700;900&family=Oswald:wght@300;400&display=swap">
<style>
:root{
  --brand:#33a6d7;
  --brand-deep:#0255a3;
  --brand-mid:#3176b5;
  --ink:#111111;
  --text:#333333;
  --muted:#555555;
  --line:#d6d6d6;
  --card:#f4f4f4;
  --blog-bg:#f4f5f7;
  --dark:#141414;
  --white:#ffffff;
}
*{box-sizing:border-box;margin:0;padding:0}
html,body{width:1200px;height:3197px;overflow:hidden}
body{font-family:"Lato",Arial,sans-serif;color:var(--text);background:var(--white);position:relative}
section,header,footer{position:absolute;left:0;width:1200px}
.abs{position:absolute}

/* header */
.site-header{top:0;height:96px;background:var(--white)}
.brand{left:80px;top:26px;display:flex;align-items:center;gap:12px;font-size:30px;font-weight:700;color:var(--brand)}
.brand-dot{width:40px;height:40px;border-radius:50%;background:var(--brand)}
.main-nav{right:70px;top:36px;display:flex;gap:14px;font-size:17px;color:var(--ink);text-transform:uppercase}
.main-nav .active{color:var(--brand)}
.main-nav .sep{color:#777}

/* hero */
.hero{top:96px;height:540px;background:linear-gradient(90deg,#0c0c0c,#1e1f22 55%,#111)}
.hero-photo{left:735px;top:0;width:373px;height:540px;background:linear-gradient(180deg,#3a3a3d,#d9c4cf 55%,#c7b3bf)}
.hero-title{left:81px;top:125px;font-family:"Oswald",Arial,sans-serif;font-weight:300;font-size:47px;line-height:58px;color:var(--white);text-transform:uppercase}
.hero-sub{left:81px;top:307px;font-size:22px;color:var(--white)}
.btn{display:inline-block;border-radius:6px;font-size:16px;text-align:center}
.btn-solid{background:var(--brand);color:var(--white)}
.btn-line{border:2px solid var(--brand);color:var(--brand);background:var(--white)}
.hero .btn{left:81px;top:364px;width:164px;height:40px;line-height:40px;font-size:18px}

/* section headings */
.sec-title{left:0;width:1200px;text-align:center;font-size:28px;font-weight:700;color:var(--ink);text-transform:uppercase}
.sec-rule{left:555px;width:90px;height:6px;border-top:2px solid var(--brand);border-bottom:1px solid var(--brand)}
.sec-sub{left:0;width:1200px;text-align:center;font-size:17px;color:var(--ink)}

/* why choose */
.why{top:636px;height:487px}
.offer{top:163px;width:354px;height:267px;background:var(--card);border:2px solid var(--line);text-align:center}
.offer h3{margin-top:50px;font-size:26px;font-weight:400;color:var(--ink)}
.offer p{margin:14px 22px 0;font-size:16px;line-height:24px;color:var(--ink)}
.offer .btn{margin-top:22px;width:128px;height:38px;line-height:34px}

/* lifecycle */
.lifecycle{top:1123px;height:497px;background:linear-gradient(180deg,#1a1c20,#2b2e33 60%,#1c1e22)}
.lifecycle .sec-title{color:var(--white);top:48px;font-size:28px}
.lifecycle .sec-sub{color:var(--white);top:108px;font-weight:700}
.step{top:198px;width:220px;text-align:center;color:var(--white)}
.step-circle{margin:0 auto;width:132px;height:132px;border-radius:50%;background:var(--brand);position:relative;display:flex;align-items:center;justify-content:center}
.step-circle.first{background:var(--white)}
.step-num{position:absolute;right:-8px;top:-2px;width:38px;height:38px;border-radius:50%;background:var(--white);border:2px solid #aaa;color:#777;font-size:17px;line-height:34px}
.step h4{margin-top:20px;font-size:19px;font-weight:400}
.step p{margin-top:8px;font-size:13px;line-height:18px}
.slider-arrow{top:220px;width:34px;height:72px;background:var(--white);display:flex;align-items:center;justify-content:center}
.dots{left:190px;top:172px}

/* platform */
.platform{top:1620px;height:564px}
.feature{width:330px}
.feature svg{display:block}
.feature h4{margin-top:8px;font-size:20px;line-height:22px;font-weight:400;color:var(--ink)}
.feature p{margin-top:12px;font-size:15px;line-height:19px;color:var(--muted)}

/* blog */
.blog{top:2184px;height:703px;background:var(--blog-bg)}
.post{top:164px;width:347px;height:482px;background:var(--white);border:1px solid var(--line)}
.post-img{height:230px}
.post-meta{margin:20px 18px 0;font-size:13px;color:var(--ink)}
.post h3{margin:18px 18px 0;font-size:20px;font-weight:400;color:var(--ink)}
.post p{margin:12px 18px 0;font-size:14px;line-height:20px;color:var(--muted)}
.post .btn{margin:24px 0 0 18px;width:112px;height:32px;line-height:28px;font-size:13px;border-radius:16px;text-transform:uppercase}

/* footer */
.site-footer{top:2887px;height:310px;background:var(--dark);color:#e5e5e5}
.foot-head{font-size:18px;color:var(--white);padding-bottom:8px;border-bottom:1px solid #888}
.foot-about{left:81px;top:40px;width:430px}
.foot-about p{margin-top:10px;font-size:14px;line-height:22px}
.contact-line{display:flex;align-items:center;gap:12px;margin-top:8px;font-size:14px}
.foot-nav{left:597px;top:40px;width:390px}
.foot-nav ul{list-style:none;display:grid;grid-template-columns:200px 190px;row-gap:24px;margin-top:14px;font-size:14px}
.foot-nav li::before{content:"→ ";color:#aaa}
.foot-nav li.active{color:var(--brand)}
.foot-social{left:1021px;top:40px;width:130px}
.foot-social ul{list-style:none;margin-top:8px;font-size:14px}
.foot-social li{display:flex;align-items:center;gap:10px;height:46px}
.foot-social .mark{width:12px;height:12px;border-radius:50%;background:#ddd}
.foot-rule{left:81px;top:252px;width:1066px;border-top:1px solid #444}
.copyright{left:0;top:274px;width:1200px;text-align:center;font-size:14px}
</style>
</head>
<body>

<header class="site-header">
  <div class="brand abs"><span class="brand-dot"></span>Brivanta</div>
  <nav class="main-nav abs">
    <span class="active">Home</span><span class="sep">/</span>
    <span>About Us</span><span class="sep">/</span>
    <span>Platform</span><span class="sep">/</span>
    <span>Partners</span><span class="sep">/</span>
    <span>Blog</span><span class="sep">/</span>
    <span>Contact Us</span>
  </nav>
</header>

<section class="hero">
  <div class="hero-photo abs" role="img" aria-label="Business professional in shirt and tie with arms crossed"></div>
  <h1 class="hero-title abs">A complete package that links<br>IoT clouds with enterprise<br>software solutions</h1>
  <p class="hero-sub abs">Instantly add connected devices to your business operations.</p>
  <a class="btn btn-solid abs">Get Started</a>
</section>

<section class="why">
  <h2 class="sec-title abs" style="top:50px">Why Choose Us</h2>
  <div class="sec-rule abs" style="top:94px"></div>
  <p class="sec-sub abs" style="top:112px">A complete package that links IoT clouds with enterprise software solutions.</p>
  <article class="offer abs" style="left:81px">
    <h3>Brivanta Connected</h3>
    <p>Lorem ipsum dolor sit amet, consectetur adipiscing elit. Nullam dapibus vestiblu mnisi ut gravidausce interdum lacus</p>
    <a class="btn btn-solid">Read More</a>
  </article>
  <article class="offer abs" style="left:448px">
    <h3>Basic</h3>
    <p>Lorem ipsum dolor sit amet, consectetur adipiscing elit. Nullam dapibus vestiblu mnisi ut gravidausce interdum lacus</p>
    <a class="btn btn-line">Read More</a>
  </article>
  <article class="offer abs" style="left:816px;width:331px">
    <h3>Legacy Product</h3>
    <p>Lorem ipsum dolor sit amet, consectetur adipiscing elit. Nullam dapibus vestiblu mnisi ut gravidausce interdum lacus</p>
    <a class="btn btn-line">Read More</a>
  </article>
</section>

<section class="lifecycle">
  <h2 class="sec-title abs">Brivanta ensures end-to-end product lifecycle management</h2>
  <p class="sec-sub abs">Closely engage with users throughout the entire process and increase customer lifetime value.</p>

  <svg class="dots abs" width="840" height="40" viewBox="0 0 840 40" aria-hidden="true">
    <g fill="none" stroke="#33a6d7" stroke-width="3" stroke-dasharray="2 8" stroke-linecap="round">
      <path d="M20 38 Q110 0 200 20"/><path d="M250 38 Q335 0 420 20"/>
      <path d="M475 38 Q565 0 650 20"/><path d="M700 38 Q780 0 860 20"/>
    </g>
  </svg>

  <div class="slider-arrow abs" style="left:30px"><svg width="14" height="22"><path d="M11 2 3 11l8 9" fill="none" stroke="#33a6d7" stroke-width="3"/></svg></div>
  <div class="slider-arrow abs" style="left:1166px"><svg width="14" height="22"><path d="M3 2l8 9-8 9" fill="none" stroke="#111" stroke-width="3"/></svg></div>

  <div class="step abs" style="left:52px">
    <div class="step-circle first"><span class="step-num">1</span>
      <svg width="64" height="64" viewBox="0 0 64 64" aria-hidden="true"><g fill="none" stroke="#33a6d7" stroke-width="7" stroke-dasharray="5 4"><circle cx="24" cy="36" r="14"/><circle cx="46" cy="18" r="9"/></g><circle cx="24" cy="36" r="5" fill="#33a6d7"/></svg>
    </div>
    <h4>Manufacture</h4>
    <p>Secure manufacturing process<br>Device traceability in ERP</p>
  </div>
  <div class="step abs" style="left:280px">
    <div class="step-circle"><span class="step-num">2</span>
      <svg width="64" height="64" viewBox="0 0 64 64" aria-hidden="true"><rect x="20" y="8" width="26" height="22" fill="#fff"/><path d="M6 44h14l10 4h14l12-8v6L44 56H28L18 52H6z" fill="#fff"/></svg>
    </div>
    <h4>Sell</h4>
    <p>End user tracking in CRM<br>Social identity for proactive<br>marketing</p>
  </div>
  <div class="step abs" style="left:502px">
    <div class="step-circle"><span class="step-num">3</span>
      <svg width="72" height="56" viewBox="0 0 72 56" aria-hidden="true"><path d="M18 48a14 14 0 0 1 0-28 18 18 0 0 1 34-4 14 14 0 0 1 4 32z" fill="#fff"/></svg>
    </div>
    <h4>Provision</h4>
    <p>Simplify consumer experience<br>during device activation<br>P2P communication via Linkora</p>
  </div>
  <div class="step abs" style="left:732px">
    <div class="step-circle"><span class="step-num">4</span>
      <svg width="64" height="64" viewBox="0 0 64 64" aria-hidden="true"><path d="M8 20 30 10l22 10v26L30 56 8 46z" fill="#fff"/><path d="M8 20l22 10 22-10M30 30v26" stroke="#33a6d7" stroke-width="2" fill="none"/><circle cx="50" cy="14" r="9" fill="#fff" stroke="#33a6d7" stroke-width="2"/><path d="M46 14l3 3 5-6" stroke="#33a6d7" stroke-width="2" fill="none"/></svg>
    </div>
    <h4>Use</h4>
    <p>Customer web portal and<br>mobile apps<br>Notifications, social identity<br>and advanced IoT services</p>
  </div>
  <div class="step abs" style="left:956px">
    <div class="step-circle"><span class="step-num">5</span>
      <svg width="64" height="64" viewBox="0 0 64 64" aria-hidden="true"><circle cx="32" cy="24" r="12" fill="#fff"/><path d="M14 58a18 16 0 0 1 36 0z" fill="#fff"/><path d="M16 26a16 16 0 0 1 32 0" stroke="#fff" stroke-width="4" fill="none"/></svg>
    </div>
    <h4>Support</h4>
    <p>In app chat, ticketing<br>system and call center<br>integration.</p>
  </div>
</section>

<section class="platform">
  <h2 class="sec-title abs" style="top:40px;font-weight:400">Platform</h2>
  <div class="sec-rule abs" style="top:84px"></div>
  <p class="sec-sub abs" style="top:102px">A complete package that links IoT clouds with enterprise software solutions.</p>

  <div class="feature abs" style="left:81px;top:160px">
    <svg width="44" height="54" aria-hidden="true"><circle cx="24" cy="8" r="6" fill="#33a6d7"/><path d="M14 18h18l-4 16 8 12h-8l-6-10-6 12H8l8-16z" fill="#33a6d7"/></svg>
    <h4>Multi-tennant<br>PaaS solution</h4>
    <p>In aliquet duiurabitur vulputate gravida ipsum quis pharetra. Integer ac viverra justorasutate</p>
  </div>
  <div class="feature abs" style="left:454px;top:160px">
    <svg width="48" height="54" aria-hidden="true"><circle cx="24" cy="22" r="20" fill="#e0e0e0" stroke="#555" stroke-width="2"/><path d="M12 26a8 8 0 0 1 4-12 10 10 0 0 1 18 2 6 6 0 0 1 2 10z" fill="#555"/><rect x="18" y="42" width="12" height="10" fill="#555"/></svg>
    <h4>Abstract device models &amp;<br>multi product support</h4>
    <p>Lorem ipsum dolor sit amet, consectetur adng elit. Duis et aliquet nibh, gravida consectetur</p>
  </div>
  <div class="feature abs" style="left:859px;top:160px">
    <svg width="50" height="54" aria-hidden="true"><g fill="#333"><ellipse cx="20" cy="8" rx="18" ry="6"/><rect x="2" y="10" width="36" height="10"/><rect x="2" y="23" width="36" height="10"/><rect x="2" y="36" width="36" height="10"/></g><circle cx="40" cy="42" r="9" fill="#777" stroke="#fff" stroke-width="2"/></svg>
    <h4>Data integration from IoT<br>Connected device clouds</h4>
    <p>nisi. Nam nunc dolor, aliquam ut odio non, dapibus efficitur odio. Cras ac pulvinar risus</p>
  </div>

  <div class="feature abs" style="left:81px;top:358px">
    <svg width="44" height="56" aria-hidden="true"><rect x="6" y="2" width="30" height="52" rx="4" fill="#333"/><rect x="10" y="8" width="22" height="38" fill="#eee"/></svg>
    <h4>Mobile Application<br>infrastructure</h4>
    <p>viverra ex, nec ullamcorper felis risus volutpat arcu. Nulla eget felis ullamcorper, euismodgue</p>
  </div>
  <div class="feature abs" style="left:454px;top:358px">
    <svg width="70" height="56" aria-hidden="true"><g fill="#555"><circle cx="20" cy="12" r="7"/><circle cx="35" cy="10" r="8"/><circle cx="50" cy="12" r="7"/><rect x="10" y="22" width="18" height="30" rx="4"/><rect x="26" y="20" width="18" height="34" rx="4" fill="#333"/><rect x="42" y="22" width="18" height="30" rx="4"/></g></svg>
    <h4>Business operations<br>Integration</h4>
    <p>Fusce rhoncus ligula metus, id luctus mauris interdum a. Nunc porta sollicitudin magna, et</p>
  </div>
  <div class="feature abs" style="left:859px;top:358px">
    <svg width="66" height="56" aria-hidden="true"><g fill="none" stroke="#333" stroke-width="7" stroke-dasharray="5 4"><circle cx="20" cy="20" r="12"/><circle cx="42" cy="38" r="10"/></g><circle cx="54" cy="14" r="6" fill="#777"/></svg>
    <h4>REST API's towards other OEM<br>integrations</h4>
    <p>fermentum ipsum. Cras a varius urna. Mauris venenatis, enim in pulvinar feugiat, elit arcu</p>
  </div>
</section>

<section class="blog">
  <h2 class="sec-title abs" style="top:48px">Latest Blog</h2>
  <p class="sec-sub abs" style="top:118px">Lorem ipsum dolor sit amet, consectetur adis cineliorbi tellus dui, vestibulum temporeugiat tinciun pellentesque</p>

  <article class="post abs" style="left:81px">
    <div class="post-img" role="img" aria-label="Hands using a tablet in front of a server room" style="background:linear-gradient(135deg,#1d3a52,#4f7d9c 50%,#2a2f3a)"></div>
    <div class="post-meta">By Admin at June 29,2017</div>
    <h3>Best Web Hosting In the World</h3>
    <p>Lorem ipsum dolor sit amet, consectetur adis cineliorbi tellus dui, vestibulum temporeugiat tinciun pellentesque vel augue. Fusce gravida</p>
    <a class="btn btn-solid">View More</a>
  </article>
  <article class="post abs" style="left:441px">
    <div class="post-img" role="img" aria-label="Technician at a network cabling rack" style="background:linear-gradient(90deg,#2d5f8f,#6f8fa8 40%,#c8b9a8 70%,#d9cfc2)"></div>
    <div class="post-meta">By Admin at June 29,2017</div>
    <h3>But I must explain to you how.</h3>
    <p>Lorem ipsum dolor sit amet, consectetur adis cineliorbi tellus dui, vestibulum temporeugiat tinciun pellentesque vel augue. Fusce gravida</p>
    <a class="btn btn-line">View More</a>
  </article>
  <article class="post abs" style="left:801px">
    <div class="post-img" role="img" aria-label="Business person touching floating cloud service icons" style="background:linear-gradient(135deg,#9aa6b0,#4c5866 55%,#2e3640)"></div>
    <div class="post-meta">By Admin at June 29,2017</div>
    <h3>We denounce with righteous.</h3>
    <p>Lorem ipsum dolor sit amet, consectetur adis cineliorbi tellus dui, vestibulum temporeugiat tinciun pellentesque vel augue. Fusce gravida</p>
    <a class="btn btn-line">View More</a>
  </article>
</section>

<footer class="site-footer">
  <div class="foot-about abs">
    <div class="foot-head" style="border:0;padding:0">Brivanta</div>
    <div style="width:160px;border-top:1px solid #888;margin-top:8px"></div>
    <p>Founded in 2016 by industry veterans, Brivanta is geared to provide integrated solutions for the IoT industry With a off-shore development center in Eastern Europe, Brivanta is positioned</p>
    <div class="contact-line"><svg width="16" height="20"><path d="M8 19C3 12 1 9 1 7a7 7 0 0 1 14 0c0 2-2 5-7 12z" fill="#33a6d7"/><circle cx="8" cy="7" r="2.5" fill="#141414"/></svg>418 Harbor Lane Westfield, CA 90210</div>
    <div class="contact-line"><svg width="16" height="16"><path d="M3 1l3 0 2 4-2 2a9 9 0 0 0 3 3l2-2 4 2v3l-2 2C7 15 1 9 1 3z" fill="#33a6d7"/></svg>+1 (555) 010-4782</div>
    <div class="contact-line"><svg width="18" height="14"><rect x="0.5" y="0.5" width="17" height="13" fill="#33a6d7"/><path d="M1 1l8 7 8-7" stroke="#141414" fill="none" stroke-width="1.5"/></svg>info@brivanta.com</div>
  </div>

  <nav class="foot-nav abs">
    <div class="foot-head" style="width:260px">Navigation</div>
    <ul>
      <li class="active">Home</li><li>Blog</li>
      <li>About Us</li><li>Sitemap</li>
      <li>Platform</li><li>Privacy</li>
      <li>Partners</li><li>Contact Us</li>
    </ul>
  </nav>

  <div class="foot-social abs">
    <div class="foot-head">Social Media</div>
    <ul>
      <li><span class="mark"></span>Chirpline</li>
      <li><span class="mark"></span>Friendwall</li>
      <li><span class="mark"></span>Circles +</li>
      <li><span class="mark"></span>Worknet</li>
    </ul>
  </div>

  <div class="foot-rule abs"></div>
  <p class="copyright abs">© Brivanta 2017</p>
</footer>

</body>
</html>
```